Orsabellitravel.com web design project + logo design

Hi,

We are a Russian online tour operator - tripwelder.com

We are looking to tranmsfer our domain to orsabellitravel.com. The website and logo need to be orsabelliesque - we are not looking to change our functionality, but we need to make the website much more attracitve to clients, much more wild looking but at the same time remaining a professional travel company.

The main concept of the website should be innovative travel (as orsabelli was an innovator). Alternatively, you could go down the artist route and go down the draw / design your own tour road.

On our website the customer is able to combine travel services (hotels, flights, Visa services, and soon chauffeur, car rental etc...) put it into their basket (the basket definitely has to look better than it is at the moment) and pay for it in one go by card.

We are also stressin our customer support with web chat, call centre etc... (call centre number at the top of the page)

We aim to provide an easy user experience, but we need to make it have some more style, so I will be waiting for what you guys can come up with.
Let me know if you have any questions - skype is: mrkolbuzov

It Company

• It is quite a simple task - to take the existing website tripwelder.com and orsabellisize it to create orsabellitravel.com, the functionality of the website will remain the same and there are not many pages in the website. Homepage, Checkout step1, Checkout step 2 (you can view both of these if you select a service) and the generic pages for T&C''s, Privacy policy etc...

IMPORTANT UPDATE

We are also looking at how the search results will look in the designs, (please do a search on our website for hotel / flight)

```html
<!DOCTYPE html>
<html lang="en">
<head>
<meta charset="utf-8">
<title>Orsabelli Travel</title>
<link href="https://fonts.googleapis.com/css2?family=Roboto:wght@300;400;500;700&display=swap" rel="stylesheet">
<style>
:root{
  --pink:#ee2a8e;
  --blue:#1ab3ef;
  --dark:#3a3a3c;
  --mid:#5a5a5c;
  --grey-bg:#ebebeb;
  --line:#d0d0d0;
  --text:#555;
  --white:#fff;
}
*{box-sizing:border-box;margin:0;padding:0}
html,body{width:756px;height:1200px;overflow:hidden;background:var(--white);font-family:'Roboto',Arial,sans-serif;color:var(--text)}
.page{position:relative;width:756px;height:1200px;overflow:hidden}
.abs{position:absolute}
.hero{left:0;top:0;width:756px;height:367px;background:linear-gradient(180deg,#2a2344 0%,#3d3357 35%,#5b4a3a 62%,#8a6a2e 75%,#2e2a30 100%)}
.brand{left:126px;top:12px;display:flex;align-items:center;gap:6px;color:var(--white);font-weight:500;font-size:21px;line-height:18px}
.brand .dot{width:34px;height:34px;border-radius:50%;background:var(--white)}
.lang{left:590px;top:12px;width:40px;height:10px;background:#eee;font-size:6px;color:#333;padding-left:3px;line-height:10px}
.phone{left:490px;top:28px;display:flex;gap:6px}
.phone .num{color:var(--white);font-size:18px;font-weight:300;line-height:20px}
.phone .hours{color:var(--pink);font-size:7px;font-weight:300}
.pill{left:584px;width:46px;height:18px;background:var(--white);font-size:6.5px;color:var(--pink);display:flex;align-items:center;justify-content:flex-end;padding-right:4px;gap:4px}
.tab{top:162px;width:56px;height:18px;font-size:7px;color:#ddd;text-align:center;line-height:18px;background:#4a4a4c}
.tab.active{background:var(--blue);color:#07334a}
.panel{left:126px;top:180px;width:372px;height:128px;background:var(--white)}
.panel .lbl{position:absolute;font-size:7px;color:var(--pink)}
.panel .sub{position:absolute;font-size:5px;color:#aaa}
.field{position:absolute;height:14px;border:2px solid #e4e4e4;font-size:6px;color:#666;padding-left:4px;line-height:10px;background:var(--white)}
.field.ph{color:#bbb}
.sel{position:absolute;height:13px;border:1px solid #ccc;font-size:6px;color:#444;padding-left:3px;line-height:11px}
.sel::after{content:"";position:absolute;right:2px;top:2px;width:7px;height:7px;background:#444}
.btn-dark{position:absolute;background:var(--dark);color:var(--white);text-align:center;border-bottom:2px solid #222}
.basket{left:502px;top:181px;width:128px;height:126px;background:var(--white)}
.basket .head{height:20px;background:var(--blue);color:#0c2a3a;font-size:12px;text-align:center;line-height:20px}
.basket .pay{position:absolute;top:73px;width:128px;height:16px;background:var(--pink);color:var(--white);font-size:7px;text-align:center;line-height:16px}
.basket .cards{position:absolute;top:89px;width:128px;height:18px;background:#6b6b6d;display:flex;justify-content:center;align-items:center;gap:4px}
.basket .cards span{width:16px;height:10px;background:#ddd;border-radius:1px}
.basket .price{position:absolute;top:107px;width:128px;height:19px;background:#4a4a4c;color:var(--white);font-size:7px;text-align:center;line-height:19px}
.booktab{left:304px;top:336px;width:148px;height:31px;background:var(--white);text-align:center;font-size:9px;color:#333;padding-top:4px}
.booktab .book{display:inline-block;margin-top:3px;background:var(--pink);color:var(--white);font-size:8px;padding:1px 5px}
.finder{left:0;top:367px;width:756px;height:92px;background:linear-gradient(180deg,#ffffff,#e6e6e6)}
.finder-line{left:0;top:459px;width:756px;height:2px;background:var(--blue)}
.step{top:383px;height:13px;background:var(--blue);color:#123;font-size:6px;line-height:13px;padding-left:4px}
.check{font-size:5.5px;color:#444;display:flex;align-items:center;gap:6px}
.check i{width:7px;height:6px;border:1px solid #bbb;background:#fff}
.date{position:absolute;width:57px;height:16px;border:1px solid #ccc;background:#fff;font-size:5.5px;color:#999;padding:4px 2px}
.spin{position:absolute;top:411px;width:40px;height:15px;border:1px solid #ccc;background:#fff;font-size:6px;color:#333;padding:3px 4px}
.tag{background:var(--mid);color:var(--white);font-size:15px;font-weight:300;padding:3px 8px;height:24px;white-space:nowrap}
.info{left:0;top:480px;width:756px;height:198px;background:var(--grey-bg)}
.h-pink{color:var(--pink);font-weight:300;text-align:center;white-space:nowrap}
.opt{font-size:12px;color:#333;text-align:center;width:200px}
.click{width:54px;height:18px;background:var(--blue);color:var(--white);font-size:7.5px;text-align:center;line-height:18px;border-bottom:2px solid #0f8fc0}
.art{left:126px;top:690px;width:506px;height:194px;background:linear-gradient(180deg,#f6fbfd,#fbeef4 60%,#f4f4f4)}
.title-box{left:225px;top:755px;width:306px;height:38px;background:var(--white);border:1px solid #ddd;font-size:23px;line-height:36px;letter-spacing:-0.3px;overflow:hidden}
.desc-box{left:126px;top:806px;width:506px;height:44px;background:var(--white);border:1px solid #ddd;font-size:6.4px;line-height:11px;color:#666;padding:3px 9px}
.hotels{left:0;top:896px;width:756px;height:166px;background:var(--grey-bg)}
.hotels p{position:absolute;left:126px;top:102px;width:500px;font-size:6.5px;line-height:11.2px;color:#666}
.footer{left:0;top:1096px;width:756px;height:84px;background:var(--blue)}
.fcol{top:1108px}
.fcol h4{font-size:8px;font-weight:400;color:#0f2a3a;margin-bottom:10px}
.fcol li{list-style:none;font-size:5.5px;color:var(--white);line-height:10px;display:flex;align-items:center;gap:4px;white-space:nowrap}
.fcol li i{width:7px;height:7px;border-radius:50%;background:var(--white)}
.offers{left:474px;top:1078px;width:156px;height:40px;background:var(--white);padding:4px 8px}
.offers h4{font-size:8.5px;font-weight:500;color:#222}
.offers .email{margin-top:5px;height:15px;border-radius:8px;background:var(--pink);position:relative;font-size:5.5px;color:#fde;padding:4px 6px}
.offers .send{position:absolute;right:0;top:0;width:44px;height:15px;background:#111;border-radius:8px;color:#fff;font-size:6.5px;text-align:center;line-height:15px}
.flogo{left:528px;top:1132px;display:flex;align-items:center;gap:5px;color:var(--white);font-size:17px;font-weight:500;line-height:14px}
.flogo .dot{width:28px;height:28px;border-radius:50%;background:var(--white)}
.bottom{left:0;top:1180px;width:756px;height:20px;background:var(--dark);color:#ccc;font-size:5.5px;text-align:center;line-height:20px}
</style>
</head>
<body>
<div class="page">

  <div class="abs hero" role="img" aria-label="Night view of a city skyline with illuminated domed towers and a lit bridge over the river"></div>

  <div class="abs brand"><span class="dot"></span><span>Orsabelli<br>Travel</span></div>
  <div class="abs lang">English ▾</div>
  <div class="abs phone">
    <svg width="20" height="22" viewBox="0 0 20 22"><path d="M4 2 L8 2 L9 7 L6 9 Q8 14 12 16 L14 13 L19 15 L18 20 Q8 21 2 8 Z" fill="#ee2a8e"/></svg>
    <div><div class="num">8-800-555-0142</div><div class="hours">(Mon-Fri) Hours: 9:00 am - 18:00</div></div>
  </div>
  <div class="abs pill" style="top:62px"><svg width="9" height="9" viewBox="0 0 10 10"><circle cx="5" cy="3" r="2.5" fill="#444"/><rect x="1" y="6" width="8" height="4" rx="2" fill="#444"/></svg>My Tour</div>
  <div class="abs pill" style="top:86px"><svg width="10" height="8" viewBox="0 0 10 8"><ellipse cx="4" cy="3" rx="4" ry="3" fill="#444"/><ellipse cx="7" cy="5" rx="3" ry="2.5" fill="#444"/></svg>Web Chat</div>

  <div class="abs tab active" style="left:126px">TICKETS</div>
  <div class="abs tab" style="left:183px">INFO</div>
  <div class="abs tab" style="left:240px">HOTELS</div>

  <div class="abs panel">
    <span class="lbl" style="left:10px;top:20px">Whence</span>
    <div class="field ph" style="left:60px;top:14px;width:104px">Type...</div>
    <span class="lbl" style="left:184px;top:18px">Where</span>
    <div class="field ph" style="left:226px;top:14px;width:104px">Type...</div>
    <span class="lbl" style="left:10px;top:42px">There</span>
    <div class="field" style="left:60px;top:36px;width:104px">30-5-2013</div>
    <span class="lbl" style="left:184px;top:42px">Back</span>
    <div class="field" style="left:226px;top:36px;width:62px">16-6-2013</div>
    <div class="check" style="position:absolute;left:293px;top:36px;font-size:5px"><i></i>Back</div>
    <div class="check" style="position:absolute;left:293px;top:45px;font-size:5px"><i></i>One way</div>
    <span class="sub" style="left:63px;top:57px">Men</span>
    <span class="sub" style="left:102px;top:57px">Women</span>
    <span class="sub" style="left:141px;top:57px">Children</span>
    <span class="lbl" style="left:10px;top:71px">Passengers</span>
    <div class="sel" style="left:60px;top:68px;width:22px">1</div>
    <div class="sel" style="left:101px;top:68px;width:22px">1</div>
    <div class="sel" style="left:141px;top:68px;width:22px">1</div>
    <span class="lbl" style="left:184px;top:71px">Class</span>
    <div class="sel" style="left:226px;top:67px;width:104px;height:14px">Economy</div>
    <div class="btn-dark" style="left:150px;top:99px;width:72px;height:22px;font-size:11px;font-weight:300;line-height:20px">Search</div>
  </div>

  <div class="abs basket">
    <div class="head">BASKET</div>
    <svg style="position:absolute;left:44px;top:24px" width="42" height="34" viewBox="0 0 42 34">
      <circle cx="3" cy="4" r="2" fill="#1ab3ef"/>
      <path d="M3 4 L9 8 L13 24 L36 24" stroke="#555" stroke-width="2" fill="none"/>
      <path d="M10 9 L39 9 L35 20 L13 20 Z" fill="none" stroke="#888" stroke-width="1.5"/>
      <circle cx="16" cy="29" r="3" fill="none" stroke="#444" stroke-width="2"/>
      <circle cx="32" cy="29" r="3" fill="none" stroke="#444" stroke-width="2"/>
    </svg>
    <div class="pay">Payment</div>
    <div class="cards"><span></span><span></span><span></span><span></span><span></span></div>
    <div class="price">*Pricing</div>
  </div>

  <div class="abs booktab">Search for A Hotel / Flight<br><span class="book">Book Now</span></div>

  <div class="abs finder"></div>
  <div class="abs finder-line"></div>
  <div class="abs step" style="left:126px;width:40px">01. What?</div>
  <div class="abs step" style="left:213px;width:40px">02. Where?</div>
  <div class="abs step" style="left:396px;width:40px">03. When?</div>
  <div class="abs step" style="left:506px;width:40px">04. Who?</div>
  <div class="abs check" style="left:126px;top:402px"><i></i>Hotels</div>
  <div class="abs check" style="left:126px;top:416px"><i></i>Flights</div>
  <div class="abs check" style="left:126px;top:430px"><i></i>Cars</div>
  <div class="sel" style="left:213px;top:402px;width:130px;height:15px;background:#fff;color:#999;font-size:5.5px;line-height:13px">Lorem Ipsum Dolor</div>
  <div class="date" style="left:397px;top:402px">Check In</div>
  <div class="date" style="left:397px;top:422px">Check Out</div>
  <div class="abs" style="left:506px;top:401px;font-size:6px;color:#333">Rooms</div>
  <div class="abs" style="left:549px;top:401px;font-size:6px;color:#333">Adults</div>
  <div class="abs" style="left:592px;top:401px;font-size:6px;color:#333">Child</div>
  <div class="spin" style="left:506px">01 <span style="float:right">⬍</span></div>
  <div class="spin" style="left:549px">01 <span style="float:right">⬍</span></div>
  <div class="spin" style="left:592px">01 <span style="float:right">⬍</span></div>
  <div class="btn-dark" style="left:570px;top:445px;width:62px;height:18px;font-size:8px;line-height:16px">Search</div>

  <div class="abs info"></div>
  <div class="abs tag" style="left:126px;top:492px;width:58px">INFO</div>
  <div class="abs h-pink" style="left:0;top:522px;width:756px;font-size:24px">There are two option apply for visa</div>
  <div class="abs opt" style="left:177px;top:573px">1. Oformlenie visa “Online”</div>
  <div class="abs opt" style="left:408px;top:573px">2. Visa “Myself.”</div>
  <svg class="abs" style="left:267px;top:604px" width="20" height="30" viewBox="0 0 20 30"><path d="M7 0 H13 V18 H20 L10 30 L0 18 H7 Z" fill="#111"/></svg>
  <svg class="abs" style="left:498px;top:604px" width="20" height="30" viewBox="0 0 20 30"><path d="M7 0 H13 V18 H20 L10 30 L0 18 H7 Z" fill="#111"/></svg>
  <div class="abs click" style="left:250px;top:643px">Click Here</div>
  <div class="abs click" style="left:481px;top:643px">Click Here</div>

  <div class="abs art" role="img" aria-label="Light line sketch of world landmarks with an airliner flying above"></div>
  <div class="abs tag" style="left:126px;top:689px;width:74px">TICKETS</div>
  <div class="abs title-box h-pink">Flights from Tours designer.</div>
  <div class="abs desc-box">On our site you can consider offers from different airlines and purchase tickets according to your wishes and budget. Plan dates of departures and arrivals c in any country, filling the cells you want, Tour Designer automatically displays your program in the calendar. On Tour Designer You can create any tour, including round-the-world and pay for all the services a single payment.</div>

  <div class="abs hotels">
    <div class="abs tag" style="left:126px;top:12px;width:74px">HOTELS</div>
    <div class="abs h-pink" style="left:0;top:50px;width:756px;font-size:24px">Hotels by City Builder.</div>
    <p>Our site offers a wide selection of hotels located in different countries and continents of the world. You can choose and book all kinds of accommodation options, according to your wishes and budget. pursue their dreams! We have created for you the most convenient framework for planning a vacation or business trip. Tour Builder saves your time now to buy a package tour you can just 3 simple steps: Choose the services Confirm requested services, payment of a single payment. A complete set of documents confirming the purchase tour package will be on our website in your personal account, send documents to "Print".</p>
  </div>

  <div class="abs footer"></div>
  <div class="abs fcol" style="left:126px"><h4>View Site</h4><ul><li>Home</li><li>About Us</li><li>Form</li><li>Contacts</li></ul></div>
  <div class="abs fcol" style="left:190px"><h4>Follow Us</h4><ul><li><i></i>Pagebook</li><li style="margin-top:3px"><i></i>Chirper</li><li style="margin-top:3px"><i></i>Blog</li></ul></div>
  <div class="abs fcol" style="left:264px"><h4>Contact Us</h4><ul><li>☏ +7 (495) 555-01-88</li><li>☏ 8-800-555-0142</li><li>✉ info@orsabellitravel.com</li></ul></div>
  <div class="abs fcol" style="left:366px"><h4>Find Us</h4><ul><li>Trip Welder Limited 14</li><li>Harrow Lane London,</li><li>N4 2QX UK</li></ul></div>
  <div class="abs offers"><h4>Exclusive Offers</h4><div class="email">Email Address<span class="send">Send</span></div></div>
  <div class="abs flogo"><span class="dot"></span><span>Orsabelli<br>Travel</span></div>
  <div class="abs bottom">© 2012–2013 OrsabelliTravel, Terms &amp; Conditions : Privacy Policy</div>

</div>
</body>
</html>
```